Business Card - Professional Minimalist - Double sided

We appreciate minimalist logo/web/collateral designs that allow design to tell a story. We want to relay a professional image/approach but throwing in a splash of modern when we’re able so long as it’s not distracting. Think 75% classic corporate, 25% modern. Open to black or white design, not sure which might look the best.

Target Market(s)

Senior executives or related government affairs contacts within the agriculture, energy, and defense industries (i.e., potential clients) but located outside of Washington, DC. Most potential clients based in DC with be familiar with both of us and our shared history.

Industry/Entity Type

Consulting

Contact Information for Business Card

Name: Derek M. Holloway
Title: Co-Founder & Partner
Address: 418 Linwood Terrace NE | Suite 2260 | Washington, D.C. 20017
Phone: (202) 555-0148
Email: Derek@BrimleyHolloway.example

Font styles to use
Serif

Colors

Designer to choose only greyscale colors for use in the design.

Requirements
Must have
• Name: Derek M. Holloway
Phone: (202) 555-0148

```html
<!DOCTYPE html>
<html lang="en">
<head>
<meta charset="utf-8">
<title>Brimley Holloway Group — Business Card</title>
<link rel="stylesheet" href="https://fonts.googleapis.com/css2?family=Cinzel:wght@400&family=Roboto:wght@400;700&display=swap">
<style>
  :root {
    --backdrop: #d8d8d8;
    --card-light: #ffffff;
    --card-dark: #2b2b2d;
    --ink: #3a3a3a;
    --ink-soft: #9a9a9a;
    --rule: #8a8a8a;
    --mark-dark: #6e6e72;
    --mark-rule-dark: #4a4a4d;
  }
  * { margin: 0; padding: 0; box-sizing: border-box; }
  html, body { width: 1200px; height: 801px; overflow: hidden; }
  body {
    background: var(--backdrop);
    display: flex;
    align-items: center;
    justify-content: center;
    gap: 40px;
    font-family: "Roboto", Arial, sans-serif;
  }
  .card {
    width: 540px;
    height: 309px;
    position: relative;
    box-shadow: 0 2px 6px rgba(0,0,0,0.12);
  }
  .card--front { background: var(--card-light); color: var(--ink); }
  .card--back { background: var(--card-dark); }

  .wordmark {
    position: absolute;
    display: flex;
    align-items: flex-start;
    gap: 10px;
  }
  .wordmark__square {
    width: 30px; height: 30px;
    flex: none;
    margin-top: 2px;
  }
  .wordmark__name {
    font-family: "Cinzel", "Times New Roman", serif;
    font-weight: 400;
    line-height: 1;
  }
  .wordmark__title { display: block; white-space: nowrap; }
  .wordmark__line {
    display: flex;
    align-items: center;
    gap: 8px;
    margin-top: 6px;
  }
  .wordmark__line::before {
    content: "";
    flex: 1;
    height: 1px;
    background: currentColor;
    opacity: 0.6;
  }
  .wordmark__sub { letter-spacing: 0.3em; }

  .card--front .wordmark { left: 26px; top: 130px; color: #55555a; }
  .card--front .wordmark__square { background: #8c8c90; }
  .card--front .wordmark__title { font-size: 19px; }
  .card--front .wordmark__sub { font-size: 8px; }

  .divider {
    position: absolute;
    left: 290px; top: 96px;
    width: 1px; height: 120px;
    background: var(--rule);
  }
  .contact {
    position: absolute;
    left: 304px; top: 96px;
    font-size: 12.5px;
    line-height: 1.45;
  }
  .contact__name { font-size: 16px; font-weight: 700; line-height: 1.2; }
  .contact__role { color: var(--ink-soft); margin-bottom: 2px; }
  .contact__row { display: flex; align-items: center; gap: 5px; }
  .contact__row svg { width: 9px; height: 9px; flex: none; fill: var(--ink); }

  .card--back .wordmark { left: 100px; top: 122px; color: var(--mark-dark); }
  .card--back .wordmark__square { width: 42px; height: 42px; background: var(--mark-rule-dark); }
  .card--back .wordmark__title { font-size: 30px; }
  .card--back .wordmark__sub { font-size: 11px; }
</style>
</head>
<body>
  <section class="card card--front" aria-label="Card front">
    <div class="wordmark">
      <span class="wordmark__square"></span>
      <div class="wordmark__name">
        <span class="wordmark__title">Brimley Holloway</span>
        <span class="wordmark__line"><span class="wordmark__sub">GROUP</span></span>
      </div>
    </div>
    <div class="divider"></div>
    <div class="contact">
      <p class="contact__name">Derek M. Holloway</p>
      <p class="contact__role">Co-Founder &amp; Partner</p>
      <p>418 Linwood Terrace NE</p>
      <p>Suite 2260 | Washington, D.C. 20017</p>
      <p class="contact__row">
        <svg viewBox="0 0 10 10" aria-hidden="true"><path d="M2 0.5 L3.8 2.6 L2.9 3.8 Q4 6 6.2 7.1 L7.4 6.2 L9.5 8 L8.3 9.5 Q3.5 9 0.5 1.7 Z"/></svg>
        (202) 555-0148
      </p>
      <p class="contact__row">
        <svg viewBox="0 0 10 10" aria-hidden="true"><path d="M0.5 2 H9.5 V8.5 H0.5 Z M0.5 2 L5 5.5 L9.5 2" stroke="#fff" stroke-width="0.8"/></svg>
        Derek@BrimleyHolloway.example
      </p>
      <p class="contact__row">
        <svg viewBox="0 0 10 10" aria-hidden="true"><circle cx="5" cy="5" r="4.6"/><path d="M0.6 5 H9.4 M5 0.4 Q2.2 5 5 9.6 M5 0.4 Q7.8 5 5 9.6" stroke="#fff" stroke-width="0.7" fill="none"/></svg>
        BrimleyHolloway.example
      </p>
    </div>
  </section>

  <section class="card card--back" aria-label="Card back">
    <div class="wordmark">
      <span class="wordmark__square"></span>
      <div class="wordmark__name">
        <span class="wordmark__title">Brimley Holloway</span>
        <span class="wordmark__line"><span class="wordmark__sub">GROUP</span></span>
      </div>
    </div>
  </section>
</body>
</html>
```